Kelderby Farm

Need a nice simple clean double sided business card that has our logo and info on:
Kelder By Farm
Martin & Lydia Okerlund
kelderbyfarm@examplemail.test
Martin: 1-555-218-4391
Lydia: 1-555-903-2657
Instagram @ kelderby_farm

Contact Information for Business Card

Martin & Lydia Okerlund kelderbyfarm@examplemail.test Martin: 1-555-218-4391 Lydia: 1-555-903-2657

```html
<!DOCTYPE html>
<html lang="en">
<head>
<meta charset="utf-8">
<title>Kelder By Farm – Business Card</title>
<link href="https://fonts.googleapis.com/css2?family=Open+Sans:wght@400&family=Source+Sans+3:wght@700&display=swap" rel="stylesheet">
<style>
  :root {
    --farm-green: #6fa537;
    --harvest-orange: #f5a82f;
    --ink: #111111;
    --paper: #ffffff;
  }
  html, body {
    margin: 0;
    padding: 0;
    overflow: hidden;
    background: var(--paper);
  }
  .canvas {
    position: relative;
    width: 904px;
    height: 1200px;
    overflow: hidden;
    background: var(--paper);
  }
  .card-front {
    position: absolute;
    left: 0; top: 0;
    width: 904px; height: 585px;
    background: var(--paper);
  }
  .brand-mark {
    position: absolute;
    left: 0; top: 0;
    width: 360px; height: 320px;
  }
  .brand-name {
    font-family: "Open Sans", sans-serif;
    font-weight: 400;
  }
  .divider {
    position: absolute;
    left: 348px; top: 109px;
    width: 2px; height: 259px;
    background: var(--ink);
  }
  .owners {
    position: absolute;
    left: 361px; top: 96px;
    margin: 0;
    font-family: "Source Sans 3", sans-serif;
    font-weight: 700;
    font-size: 52px;
    letter-spacing: -2.2px;
    line-height: 1;
    color: var(--farm-green);
    white-space: nowrap;
  }
  .contact {
    position: absolute;
    left: 0; top: 0;
    margin: 0; padding: 0;
    list-style: none;
    font-family: "Open Sans", sans-serif;
    font-size: 26px;
    color: var(--ink);
  }
  .contact-line {
    position: absolute;
    white-space: nowrap;
    line-height: 1;
  }
  .contact-icon {
    position: absolute;
  }
  .wave {
    position: absolute;
    left: 0; top: 429px;
    width: 904px; height: 156px;
    display: block;
  }
  .card-back {
    position: absolute;
    left: 0; top: 610px;
    width: 904px; height: 590px;
    background: var(--farm-green);
  }
  .back-mark {
    position: absolute;
    left: 0; top: 0;
    width: 904px; height: 500px;
  }
  .accent-band {
    position: absolute;
    left: 0; top: 503px;
    width: 904px; height: 57px;
    background: var(--harvest-orange);
  }
</style>
</head>
<body>
<main class="canvas">

  <section class="card-front" aria-label="Business card front">
    <svg class="brand-mark" viewBox="0 0 360 320" aria-label="Kelder By Farm">
      <circle cx="188" cy="194" r="55" fill="none" stroke="var(--farm-green)" stroke-width="3"/>
      <text class="brand-name" x="189" y="284" font-size="28" text-anchor="middle" fill="var(--farm-green)">KELDER BY FARM</text>
    </svg>

    <div class="divider"></div>

    <h1 class="owners">Martin &amp; Lydia Okerlund</h1>

    <ul class="contact">
      <li>
        <svg class="contact-icon" style="left:363px;top:194px" width="28" height="30" viewBox="0 0 28 30" aria-hidden="true">
          <path d="M20 3 C14 1 7 8 4 16 C2 22 3 27 6 28 L10 25 L8 20 L5 21 C5 15 9 9 14 7 L15 10 L20 9 L22 5 Z" fill="none" stroke="var(--ink)" stroke-width="2" stroke-linejoin="round"/>
        </svg>
        <span class="contact-line" style="left:399px;top:197px">Martin: 1-555-218-4391</span>
        <span class="contact-line" style="left:399px;top:233px">Lydia: 1-555-903-2657</span>
      </li>
      <li>
        <svg class="contact-icon" style="left:363px;top:285px" width="26" height="20" viewBox="0 0 26 20" aria-hidden="true">
          <rect x="1.5" y="1.5" width="23" height="17" fill="none" stroke="var(--ink)" stroke-width="3"/>
          <path d="M2 3 L13 12 L24 3" fill="none" stroke="var(--ink)" stroke-width="3"/>
        </svg>
        <span class="contact-line" style="left:395px;top:282px">kelderbyfarm@examplemail.test</span>
      </li>
      <li>
        <svg class="contact-icon" style="left:363px;top:343px" width="24" height="24" viewBox="0 0 24 24" aria-hidden="true">
          <rect x="1.5" y="1.5" width="21" height="21" fill="none" stroke="var(--ink)" stroke-width="2.5"/>
        </svg>
        <span class="contact-line" style="left:394px;top:343px">Instagram @ kelderby_farm</span>
      </li>
    </ul>

    <svg class="wave" viewBox="0 569 1200 207" preserveAspectRatio="none" aria-hidden="true">
      <path d="M0 686 C200 630 450 640 800 686 C950 702 1100 650 1200 598 L1200 776 L0 776 Z" fill="var(--farm-green)"/>
      <path d="M0 620 C200 575 400 585 700 650 C800 668 900 662 1000 652 C1080 640 1150 600 1200 582 C1120 620 1000 662 850 668 C700 674 500 622 300 622 C180 622 80 650 0 680 Z" fill="var(--farm-green)"/>
      <path d="M0 648 C150 605 350 597 600 640 C700 656 800 660 880 655 C780 666 700 662 600 650 C400 618 200 622 0 666 Z" fill="var(--harvest-orange)"/>
    </svg>
  </section>

  <section class="card-back" aria-label="Business card back">
    <svg class="back-mark" viewBox="0 0 904 500" aria-label="Kelder By Farm">
      <circle cx="452" cy="245" r="108" fill="none" stroke="var(--paper)" stroke-width="7.5"/>
      <text class="brand-name" x="452" y="420" font-size="54" text-anchor="middle" fill="var(--paper)">KELDER BY FARM</text>
    </svg>
    <div class="accent-band"></div>
  </section>

</main>
</body>
</html>
```